Wealth management Facebook Advertisement

Hello, we are trying to capture more leads to our online booking link through Facebook advertisement. We want an attractive modern design to get more clients and catch the attention of high net-worth clients. We deal with high-net-worth retirees, business owners, farmers, and wealth transfer. We offer high-net-worth client solutions that cover Financial Planning, Retirement and Estate Planning, Investment Planning, Tax Planning, and Insurance Planning. The final design that we would be looking for is modern and eye-catching and makes the prospective clients want to click our meeting link to schedule an introductory consultation.

We are in the Wealth Management / Financial Planning industry

Our online booking link Is the following :

https://bookings.qvnfinancial-demo.net/calendar/OliverBrandtAssociatesQLPrivateWealth@qvnfinancial-demo.net/bookings/

Our current Facebook page is the following:

https://www.sociopage-demo.net/BrandtPrivateWealth

Please ask any further questions for needed information for creating design

```html
<!DOCTYPE html>
<html lang="en">
<head>
<meta charset="utf-8">
<title>Protect and Build Your Wealth — Oliver Brandt &amp; Associates</title>
<link href="https://fonts.googleapis.com/css2?family=Lato:ital,wght@0,400;0,700;0,900;1,900&display=swap" rel="stylesheet">
<style>
  :root {
    --canvas: #ffffff;
    --ink: #2a2a28;
    --brand-navy: #1f2f6b;
    --glow: #fff6cf;
    --leaf-light: #e4e6a6;
    --leaf-mid: #a9c46a;
    --leaf-deep: #5f8a3a;
    --leaf-dark: #4a6e2c;
    --coin-light: #e2d3bb;
    --coin: #b89f80;
    --coin-dark: #7a6450;
    --badge: #ffffff;
  }
  html, body {
    margin: 0;
    padding: 0;
    width: 1200px;
    height: 628px;
    overflow: hidden;
    background: var(--canvas);
  }
  .ad {
    position: relative;
    width: 1200px;
    height: 628px;
    background: var(--canvas);
    font-family: "Lato", Arial, sans-serif;
    color: var(--ink);
    overflow: hidden;
  }
  .hero-photo {
    position: absolute;
    left: 296px;
    top: 25px;
    width: 880px;
    height: 578px;
    background:
      /* jar of coins, right */
      radial-gradient(ellipse 140px 170px at 77% 78%, var(--coin-light) 0%, var(--coin) 45%, rgba(184,159,128,0) 100%),
      /* coin stacks rising to the right */
      radial-gradient(ellipse 70px 110px at 51% 88%, var(--coin) 0%, rgba(184,159,128,0) 100%),
      radial-gradient(ellipse 60px 80px at 37% 92%, var(--coin) 0%, rgba(184,159,128,0) 100%),
      radial-gradient(ellipse 60px 60px at 24% 95%, var(--coin-light) 0%, rgba(226,211,187,0) 100%),
      radial-gradient(ellipse 60px 45px at 10% 96%, var(--coin-light) 0%, rgba(226,211,187,0) 100%),
      /* seedlings zone */
      radial-gradient(ellipse 120px 170px at 77% 30%, rgba(140,200,70,0.9) 0%, rgba(140,200,70,0) 100%),
      radial-gradient(ellipse 70px 90px at 52% 50%, rgba(140,200,70,0.85) 0%, rgba(140,200,70,0) 100%),
      radial-gradient(ellipse 55px 70px at 38% 65%, rgba(140,200,70,0.8) 0%, rgba(140,200,70,0) 100%),
      /* bokeh highlights */
      radial-gradient(circle 110px at 88% 12%, var(--glow) 0%, rgba(255,246,207,0) 100%),
      radial-gradient(circle 40px at 96% 32%, rgba(255,250,220,0.7) 0%, rgba(255,250,220,0) 100%),
      radial-gradient(circle 50px at 30% 20%, rgba(240,240,190,0.6) 0%, rgba(240,240,190,0) 100%),
      radial-gradient(ellipse 260px 180px at 50% 35%, var(--leaf-dark), rgba(74,110,44,0) 75%),
      linear-gradient(170deg, var(--leaf-light) 0%, var(--leaf-mid) 35%, var(--leaf-deep) 65%, var(--coin) 100%);
  }
  .hero-photo::after {
    content: "";
    position: absolute;
    inset: 0;
    background: linear-gradient(90deg, var(--canvas) 0%, rgba(255,255,255,0.8) 10%, rgba(255,255,255,0) 30%);
  }
  .headline {
    position: absolute;
    left: 44px;
    top: 38px;
    margin: 0;
    font-weight: 700;
    font-size: 86px;
    line-height: 88px;
    letter-spacing: -0.3px;
    color: var(--ink);
  }
  .services {
    position: absolute;
    left: 44px;
    top: 326px;
    width: 310px;
    margin: 0;
    font-size: 17.5px;
    line-height: 28px;
    font-weight: 400;
    color: var(--ink);
  }
  .brand {
    position: absolute;
    left: 44px;
    top: 496px;
    display: flex;
    align-items: flex-start;
    gap: 12px;
  }
  .brand-mark {
    width: 66px;
    height: 58px;
    background: var(--brand-navy);
    flex: none;
  }
  .brand-name {
    margin: 0;
    font-weight: 700;
    font-size: 21px;
    line-height: 24px;
    color: var(--brand-navy);
    text-transform: uppercase;
  }
  .brand-name .firm {
    display: block;
    margin-top: 10px;
  }
  .book-now {
    position: absolute;
    left: 1035px;
    top: 475px;
    width: 108px;
    height: 108px;
    border-radius: 50%;
    background: var(--badge);
    display: flex;
    align-items: center;
    justify-content: center;
    text-align: center;
    font-style: italic;
    font-weight: 900;
    font-size: 27px;
    line-height: 27px;
    color: #111;
    text-decoration: none;
  }
</style>
</head>
<body>
  <main class="ad">
    <div class="hero-photo" role="img" aria-label="Soft green bokeh background with rising stacks of coins topped by young seedlings and a glass jar full of coins with a plant growing from it"></div>

    <h1 class="headline">Let's Protect<br>and Build<br>Your Wealth</h1>

    <p class="services">We offer solutions that cover Financial Planning, Retirement and Estate Planning, Investment Planning, Tax Planning, and Insurance Planning.</p>

    <div class="brand">
      <span class="brand-mark" aria-hidden="true"></span>
      <p class="brand-name">QL Private Wealth<br>Management<span class="firm">Oliver Brandt<br>&amp; Associates</span></p>
    </div>

    <a class="book-now" href="https://bookings.qvnfinancial-demo.net/calendar/OliverBrandtAssociatesQLPrivateWealth@qvnfinancial-demo.net/bookings/">Book<br>Now</a>
  </main>
</body>
</html>
```